Stationery including letterhead, business cards, for a new Chartered Accounting Practice

I need a new set of stationery including letterhead, business cards, for a new Chartered Accounting Practice based in Melbourne, Victoria, Australia called "Brint Holloway, Chartered Accountant".

I will be providing Auditing and general consulting advice to small and medium business enterprises. The final design should communicate trust, wisdom and security.

Target Market(s)

Target Market English speaking, Australians. Proprietors small and medium sized businesses - aged 45-65. Fellow professionals - lawyers, investment consultants, other accountants. Retirees - aged 60 and over

Industry/Entity Type

Accountant

Font styles to use
Serif

Colors
0355a3

Requirements
Must have
• The final design should convey trust, wisdom and security.
• Names of practice "Brint Holloway , Chartered Accountant"
• Contact details:
• Address 284 Marbury Street, Tallow Creek, Victoria, 3172, Australia
• Telephone: 047 000 3158
• Email: brintholloway@postquill.example
Nice to have
• an expensive and professional design, the letterhead should be timeless with a logo on white space
Should not have
• no bright/fluro colours

```html
<!DOCTYPE html>
<html lang="en">
<head>
<meta charset="utf-8">
<title>Brint Holloway, Chartered Accountant – Business Cards</title>
<link rel="stylesheet" href="https://fonts.googleapis.com/css2?family=Jost:wght@400;500&family=Source+Sans+3:wght@400&display=swap">
<style>
  :root {
    --backdrop: #5f5f5f;
    --card-dark: #2a2a2a;
    --card-light: #ffffff;
    --ink-light: #f2f2f2;
    --ink-soft: #e2e2e2;
    --ink-dark: #222222;
    --watermark: #e9e9e9;
  }
  html, body {
    margin: 0;
    width: 1200px;
    height: 900px;
    overflow: hidden;
    background: var(--backdrop);
  }
  .stage {
    position: relative;
    width: 1200px;
    height: 900px;
    background: radial-gradient(ellipse at center, #656565 0%, var(--backdrop) 70%);
  }
  .card {
    position: absolute;
    top: 306px;
    width: 440px;
    height: 271px;
    overflow: hidden;
    box-shadow: 0 1px 3px rgba(0,0,0,0.25);
  }
  .card-front { left: 149px; background: var(--card-light); }
  .card-back { left: 608px; background: var(--card-dark); }

  .front-band {
    position: absolute;
    left: 0; top: 0;
    width: 100%;
    height: 110px;
    background: var(--card-dark);
  }
  .holder-name {
    font-family: "Jost", sans-serif;
    font-weight: 500;
    font-size: 31px;
    line-height: 1;
    margin: 0;
    letter-spacing: 0.3px;
  }
  .holder-title {
    font-family: "Jost", sans-serif;
    font-weight: 400;
    font-size: 12px;
    letter-spacing: 3.7px;
    margin: 0;
  }
  .front-band .holder-name {
    position: absolute; left: 24px; top: 36px; color: var(--ink-light);
  }
  .front-band .holder-title {
    position: absolute; left: 24px; top: 69px; color: var(--ink-light);
  }

  .front-watermark {
    position: absolute;
    right: 16px;
    top: 150px;
    font-family: "Jost", sans-serif;
    font-weight: 500;
    font-size: 36px;
    line-height: 0.95;
    text-align: right;
    color: var(--watermark);
    margin: 0;
  }
  .contact {
    position: absolute;
    left: 24px;
    top: 167px;
    font-family: "Source Sans 3", sans-serif;
    font-size: 12.5px;
    color: var(--ink-dark);
    line-height: 16px;
  }
  .contact-line { display: flex; align-items: center; gap: 4px; }
  .contact-line svg { width: 9px; height: 9px; fill: var(--ink-dark); }
  .contact-address { margin-top: 13px; line-height: 15.5px; }

  .back-content {
    position: absolute;
    left: 0; right: 0;
    top: 66px;
    text-align: center;
  }
  .back-wordmark {
    font-family: "Jost", sans-serif;
    font-weight: 500;
    font-size: 30px;
    color: var(--ink-soft);
    margin: 0 0 30px;
    line-height: 1;
  }
  .back-content .holder-name { color: var(--ink-soft); font-size: 32px; }
  .back-content .holder-title { color: var(--ink-soft); margin-top: 4px; letter-spacing: 4px; }
</style>
</head>
<body>
<main class="stage">
  <section class="card card-front" aria-label="Business card front">
    <header class="front-band">
      <h1 class="holder-name">BRINT HOLLOWAY</h1>
      <p class="holder-title">CHARTERED ACCOUNTANT</p>
    </header>
    <p class="front-watermark">Brint<br>Holloway</p>
    <address class="contact">
      <div class="contact-line">
        <svg viewBox="0 0 10 10" aria-hidden="true"><path d="M2.2 0.5 L3.6 2.6 L2.8 3.6 C3.4 4.9 4.9 6.5 6.4 7.2 L7.4 6.4 L9.5 7.8 L8.6 9.4 C4.5 9.2 0.8 5.5 0.6 1.4 Z"/></svg>
        <span>047 000 3158</span>
      </div>
      <div class="contact-line">
        <svg viewBox="0 0 10 10" aria-hidden="true"><path d="M0.5 2 H9.5 V8.5 H0.5 Z M1.2 2.6 L5 5.6 L8.8 2.6 Z" fill-rule="evenodd"/></svg>
        <span>brintholloway@postquill.example</span>
      </div>
      <div class="contact-address">284 Marbury Street,<br>Tallow Creek, Victoria, 3172, Australia</div>
    </address>
  </section>

  <section class="card card-back" aria-label="Business card back">
    <div class="back-content">
      <p class="back-wordmark">Brint Holloway</p>
      <h2 class="holder-name">BRINT HOLLOWAY</h2>
      <p class="holder-title">CHARTERED ACCOUNTANT</p>
    </div>
  </section>
</main>
</body>
</html>
```